i need a US celebrity blog design

hi, i need a blog which have US celebrity news. My blog should be attractive and mature with a good theme. Readers of my blog should be able to comment. You can include any attractive colour (blue, green, purple, red).

Target Market(s)

Celebrity fans and enthusiasts

Industry/Entity Type

News

```html
<!DOCTYPE html>
<html lang="en">
<head>
<meta charset="utf-8">
<title>Lumora — Celebrity Blog</title>
<link rel="stylesheet" href="https://fonts.googleapis.com/css2?family=Open+Sans:ital,wght@0,400;0,600;0,700;1,400&family=Dancing+Script&display=swap">
<style>
  :root {
    --black: #000000;
    --page: #f7f7f7;
    --red: #e5000f;
    --ink: #111111;
    --muted: #666666;
    --white: #ffffff;
  }
  * { margin: 0; padding: 0; box-sizing: border-box; }
  html, body { width: 1200px; height: 1000px; overflow: hidden; }
  body {
    position: relative;
    background: var(--page);
    font-family: "Open Sans", Arial, sans-serif;
    color: var(--ink);
  }
  .site-nav {
    position: absolute; left: 0; top: 0; width: 1200px; height: 62px;
    background: var(--black);
  }
  .site-nav ul {
    list-style: none; display: flex; position: absolute; left: 355px; top: 24px;
  }
  .site-nav li {
    font-size: 10px; font-weight: 700; color: var(--white);
    margin-right: 20px; letter-spacing: 0; position: relative; line-height: 14px;
  }
  .site-nav li.is-active { color: var(--red); }
  .site-nav li.is-active::after {
    content: ""; position: absolute; left: 0; right: 0; top: 17px;
    height: 2px; background: var(--red);
  }
  .masthead { position: absolute; left: 0; top: 62px; width: 1200px; height: 171px; text-align: center; }
  .masthead .since { position: absolute; top: 44px; width: 100%; font-size: 10.5px; color: var(--muted); letter-spacing: 0.4px; }
  .masthead .wordmark { position: absolute; top: 57px; width: 100%; font-size: 41px; font-weight: 400; color: var(--ink); letter-spacing: 1px; line-height: 1.3; }
  .masthead .tagline { position: absolute; top: 110px; left: 0; width: 1208px; font-family: "Dancing Script", cursive; font-size: 14px; color: var(--muted); }
  .featured { position: absolute; left: 0; top: 233px; width: 1200px; height: 249px; display: flex; }
  .feature { position: relative; width: 400px; height: 249px; }
  .feature-photo { position: absolute; inset: 0; }
  .feature--garden .feature-photo { background: radial-gradient(ellipse at 30% 45%, #7a1418 0%, #3a1a1a 22%, transparent 42%), linear-gradient(135deg, #0f2b22 0%, #1f4a35 45%, #0c2219 100%); }
  .feature--birds .feature-photo { background: linear-gradient(180deg, #cfcfcf 0%, #9a9a9a 45%, #3b3b3b 70%, #6a6a6a 100%); }
  .feature--street .feature-photo { background: linear-gradient(90deg, #cfc9c2 0%, #8a7f74 35%, #4c4036 60%, #b8ada2 85%, #d8d2cc 100%); }
  .feature svg { position: absolute; left: 0; top: 0; }
  .feature-label { font-family: "Open Sans", Arial, sans-serif; font-size: 13px; }
  .story-title { position: absolute; top: 522px; width: 1200px; text-align: center; font-size: 39px; font-weight: 700; color: var(--red); letter-spacing: 0.5px; line-height: 1.3; }
  .story-text { position: absolute; left: 229px; top: 587px; font-size: 10.3px; line-height: 22px; color: var(--ink); white-space: nowrap; }
  .story-text span { display: block; }
  .story-photo {
    position: absolute; left: 229px; top: 668px; width: 743px; height: 318px;
    background: radial-gradient(ellipse at 26% 55%, #3a3029 0%, #1a1a1a 30%, transparent 55%), linear-gradient(90deg, #2a2a2a 0%, #4d4d4d 40%, #2e2e2e 65%, #6a6a6a 100%);
  }
  .story-caption { position: absolute; bottom: 2px; font-size: 9.5px; font-style: italic; color: var(--red); white-space: nowrap; }
  .story-caption--left { left: 11px; }
  .story-caption--right { right: 4px; }
</style>
</head>
<body>
  <nav class="site-nav">
    <ul>
      <li class="is-active">NEWS</li>
      <li>VAULT</li>
      <li>PASSION</li>
      <li>TOUR &amp; EVENTS</li>
      <li>MUSIC</li>
      <li>MEDIA</li>
      <li>SHOP</li>
    </ul>
  </nav>

  <header class="masthead">
    <p class="since">SINCE 2010</p>
    <h1 class="wordmark">LUMORA</h1>
    <p class="tagline">Blog for konw more about me</p>
  </header>

  <section class="featured">
    <article class="feature feature--garden">
      <div class="feature-photo" role="img" aria-label="Model in a red gown lying among dark green jungle leaves"></div>
      <svg width="400" height="249" viewBox="0 0 400 249">
        <line x1="0" y1="213" x2="90" y2="213" stroke="#fff" stroke-width="1.2"/>
        <line x1="312" y1="213" x2="400" y2="213" stroke="#fff" stroke-width="1.2"/>
        <polygon points="90,213 110,197 292,197 312,213 292,229 110,229" fill="none" stroke="#fff" stroke-width="1.4"/>
        <text class="feature-label" x="201" y="218" fill="#fff" text-anchor="middle">AN OUTSIDE PHOTOSHOOTING</text>
      </svg>
    </article>
    <article class="feature feature--birds">
      <div class="feature-photo" role="img" aria-label="Black and white street scene with a model and birds in flight"></div>
      <svg width="400" height="249" viewBox="0 0 400 249">
        <line x1="0" y1="160" x2="90" y2="160" stroke="#fff" stroke-width="1.2"/>
        <line x1="310" y1="160" x2="400" y2="160" stroke="#fff" stroke-width="1.2"/>
        <polygon points="90,160 108,144 292,144 310,160 292,176 108,176" fill="rgba(0,0,0,0.35)" stroke="#fff" stroke-width="1.4"/>
        <text class="feature-label" x="200" y="165" fill="#e5000f" font-weight="600" text-anchor="middle">MODELING IN THE NATURE</text>
      </svg>
    </article>
    <article class="feature feature--street">
      <div class="feature-photo" role="img" aria-label="Blonde model in a black jacket leaning on a stone wall in a city street"></div>
      <svg width="400" height="249" viewBox="0 0 400 249">
        <line x1="0" y1="213" x2="90" y2="213" stroke="#fff" stroke-width="1.2"/>
        <line x1="310" y1="213" x2="400" y2="213" stroke="#fff" stroke-width="1.2"/>
        <polygon points="90,213 110,197 290,197 310,213 290,229 110,229" fill="none" stroke="#fff" stroke-width="1.4"/>
        <text class="feature-label" x="199" y="218" fill="#fff" text-anchor="middle">BACK TO THE 70'S WITH US</text>
      </svg>
    </article>
  </section>

  <main>
    <h2 class="story-title">MY STORY</h2>
    <p class="story-text">
      <span>Sometimes great ideas come out of the simplest things. Lorem ipsum dolor sit amet, consectetuer adipiscing elit, sed diam nonummy nibh euismod volutpat.</span>
      <span>Ut wisi enim ad miinim veniam, quis nostrud exerci tation ullamcorper suscipit lobortis nisl ut aliquip ex ea commodo conseq valto. duis autem</span>
      <span>vel eum iriure dolor in hendrerit in vulputate velit esse molestic consequat, vel ibh euismod tincidunt.</span>
    </p>
    <figure class="story-photo" role="img" aria-label="Black and white portrait of a woman in a leather jacket beside a row of parked cars">
      <figcaption class="story-caption story-caption--left">"Lumora was made from love about Passion"</figcaption>
      <figcaption class="story-caption story-caption--right">"Our story is a neverending one"</figcaption>
    </figure>
  </main>
</body>
</html>
```